Bref créative
Business Cards and Stationery Project
Verdant Pathways Health and Fitness Center
I need double sided standard sized Business Card [3.5" x 2"]
Use same fonts as used on my logo but also try different fonts
Professional
Marcus T. Delaney
Owner/Health Practitioner
4172 Larchmont Ave S
Fairhaven, MN 55990
marcus.delaney@vpwellbody.com
www.vpwellbody.com
Looking for a clean looking business card/stationery. It would be nice to have health center tagline w/ company name one one side. Tagline Where Everyday Wellness Becomes Lasting Strength. If possible can there be date and time space for appointment.

```html
<!DOCTYPE html>
<html lang="en">
<head>
<meta charset="utf-8">
<title>Verdant Pathways Health and Fitness Center — Business Card</title>
<link rel="stylesheet" href="https://fonts.googleapis.com/css2?family=PT+Serif:ital,wght@0,400;0,700;1,700&display=swap">
<style>
  :root {
    --page-bg: #e9e6e1;
    --card-white: #ffffff;
    --brand-navy: #1f3f86;
    --rule-blue: #2b4fa0;
    --green-light: #a6cf3a;
    --green-mid: #8dbd1f;
    --green-deep: #6d9d12;
    --text-on-green: #ffffff;
  }
  * { box-sizing: border-box; margin: 0; padding: 0; }
  html, body {
    width: 1200px; height: 780px; overflow: hidden;
    background: var(--page-bg);
    font-family: "PT Serif", Georgia, serif;
  }
  .card {
    position: absolute; left: 75px; top: 90px;
    width: 1050px; height: 600px;
    border-radius: 34px; overflow: hidden;
    background: var(--card-white);
    box-shadow: 0 10px 30px rgba(0,0,0,.18);
  }
  .brand {
    position: absolute; top: 88px; left: 0; right: 0;
    display: flex; justify-content: center; align-items: center; gap: 22px;
  }
  .brand-dot {
    width: 54px; height: 54px; border-radius: 50%;
    background: var(--green-mid);
  }
  .brand-name {
    color: var(--brand-navy); font-weight: 700; line-height: 1.05;
  }
  .brand-name .primary { display: block; font-size: 50px; letter-spacing: 1px; }
  .brand-name .secondary { display: block; font-size: 21px; letter-spacing: 1.5px; text-transform: uppercase; }
  .tagline {
    position: absolute; top: 214px; left: 0; right: 0;
    text-align: center; color: var(--brand-navy);
    font-style: italic; font-weight: 700; font-size: 22px; letter-spacing: .5px;
  }
  .rule {
    position: absolute; top: 268px; left: 0; right: 0;
    height: 4px; background: var(--rule-blue);
  }
  .contact-band {
    position: absolute; top: 276px; left: 0; right: 0; bottom: 0;
    background: linear-gradient(180deg, var(--green-light) 0%, var(--green-mid) 55%, var(--green-deep) 100%);
    color: var(--text-on-green);
  }
  .person {
    position: absolute; top: 108px; right: 580px; text-align: right;
  }
  .person-name { font-weight: 700; font-size: 34px; }
  .person-title { font-size: 24px; margin-top: 6px; }
  .divider {
    position: absolute; top: 50px; left: 505px;
    width: 2px; height: 230px; background: rgba(255,255,255,.8);
  }
  .details {
    position: absolute; top: 52px; left: 540px;
    font-size: 22px; line-height: 1.35;
  }
  .address { margin-bottom: 28px; }
  .detail-row { display: flex; align-items: center; gap: 14px; margin-bottom: 10px; }
  .detail-row svg { flex: none; }
</style>
</head>
<body>
  <main class="card">
    <header class="brand">
      <span class="brand-dot"></span>
      <div class="brand-name">
        <span class="primary">Verdant Pathways</span>
        <span class="secondary">Health and Fitness Center</span>
      </div>
    </header>
    <p class="tagline">Where Everyday Wellness Becomes Lasting Strength</p>
    <div class="rule"></div>
    <section class="contact-band">
      <div class="person">
        <p class="person-name">Marcus T. Delaney</p>
        <p class="person-title">Owner/Health Practitioner</p>
      </div>
      <div class="divider"></div>
      <div class="details">
        <p class="address">4172 Larchmont Ave S<br>Fairhaven, MN 55990</p>
        <p class="detail-row">
          <svg width="14" height="24" viewBox="0 0 14 24" aria-hidden="true">
            <rect x="1" y="1" width="12" height="22" rx="2" fill="none" stroke="#fff" stroke-width="2"/>
            <circle cx="7" cy="19" r="1.5" fill="#fff"/>
          </svg>
          <span>612-555-0148</span>
        </p>
        <p class="detail-row">
          <svg width="18" height="14" viewBox="0 0 18 14" aria-hidden="true">
            <rect x="1" y="1" width="16" height="12" fill="none" stroke="#fff" stroke-width="2"/>
            <path d="M1 1 L9 8 L17 1" fill="none" stroke="#fff" stroke-width="2"/>
          </svg>
          <span>marcus.delaney@vpwellbody.com</span>
        </p>
      </div>
    </section>
  </main>
</body>
</html>
```